Business Card Design

We need the business card for our new business based in St. Marys, we manufacture mainly bubble wraps. And we would like the design to use our company logo and also make it easy for people to understand right away we are bubble wrap manufacturer

Industry/Entity Type

Business

Contact Information for Business Card

Cushora Pty Ltd, 14 Harlow Lane Kellbrook NSW 2791, Tel: 02 9715 4826, Fax: 9715 4839, Dale Omar, General Manager, Mobile :0427 351 604, dale.omar@cushora.com.au, Website: cushora.com.au

```html
<!DOCTYPE html>
<html lang="en">
<head>
<meta charset="utf-8">
<title>Cushora Business Card</title>
<link rel="stylesheet" href="https://fonts.googleapis.com/css2?family=Montserrat:wght@400;500;700;800&display=swap">
<style>
  :root {
    --backdrop: #dcdcdc;
    --card: #ffffff;
    --ink-grey: #5f5f5f;
    --ink-soft: #7a7a7a;
    --brand-red: #b8231f;
    --band-grey: #7b7b7b;
  }
  * { box-sizing: border-box; margin: 0; padding: 0; }
  html, body {
    width: 1200px; height: 852px; overflow: hidden;
    background: var(--backdrop);
    font-family: "Montserrat", Arial, sans-serif;
  }
  .stage { position: relative; width: 1200px; height: 852px; }
  .card {
    position: absolute; width: 480px; height: 274px;
    background: var(--card); border-radius: 12px; overflow: hidden;
    box-shadow: 0 6px 18px rgba(0,0,0,0.18);
  }
  .card--front { left: 120px; top: 130px; }
  .card--back  { left: 600px; top: 440px; }

  .wordmark {
    color: var(--ink-grey); font-weight: 800; letter-spacing: 1px; line-height: 1;
  }
  .tagline {
    color: var(--ink-soft); font-weight: 500; text-transform: uppercase;
    letter-spacing: 3.4px; line-height: 1;
  }
  .card--front .brand {
    position: absolute; left: 0; right: 0; top: 96px; text-align: center;
  }
  .card--front .wordmark { font-size: 58px; }
  .card--front .tagline { font-size: 11.5px; margin-top: 10px; }

  .card--back .brand {
    position: absolute; right: 26px; top: 26px; text-align: right;
  }
  .card--back .wordmark { font-size: 34px; }
  .card--back .tagline { font-size: 7px; letter-spacing: 2px; margin-top: 5px; }

  .person { position: absolute; left: 26px; top: 92px; }
  .person__name {
    color: var(--brand-red); font-weight: 700; font-size: 14px; letter-spacing: 0.5px;
  }
  .person__role { color: var(--ink-soft); font-size: 10px; margin-top: 3px; }

  .address {
    position: absolute; left: 26px; top: 150px;
    color: var(--ink-soft); font-size: 10.5px;
  }
  .contacts {
    position: absolute; left: 26px; top: 168px; list-style: none;
  }
  .contacts li {
    display: flex; align-items: center; gap: 8px;
    color: var(--ink-soft); font-size: 10.5px; height: 14px;
  }
  .contacts svg { width: 10px; height: 10px; fill: var(--brand-red); flex: none; }

  .corner-bands { position: absolute; left: 0; bottom: 0; width: 480px; height: 60px; }
</style>
</head>
<body>
<main class="stage">
  <section class="card card--front" aria-label="Card front">
    <div class="brand">
      <div class="wordmark">CUSHORA</div>
      <div class="tagline">Cushioned Bubble Wrap Makers</div>
    </div>
  </section>

  <section class="card card--back" aria-label="Card back">
    <div class="brand">
      <div class="wordmark">CUSHORA</div>
      <div class="tagline">Cushioned Bubble Wrap Makers</div>
    </div>

    <div class="person">
      <div class="person__name">DALE OMAR</div>
      <div class="person__role">General Manager</div>
    </div>

    <p class="address">14 Harlow Lane Kellbrook NSW 2791</p>

    <ul class="contacts">
      <li>
        <svg viewBox="0 0 10 10" aria-hidden="true"><path d="M1 3c0-1 1-2 2-2h4c1 0 2 1 2 2v1H7V3H3v1H1zM2 5h6l1 4H1z"/></svg>
        02 9715 4826
      </li>
      <li>
        <svg viewBox="0 0 10 10" aria-hidden="true"><path d="M3 0h4v3H3zM1 3h8v5H7v2H3V8H1zM4 7v2h2V7z"/></svg>
        9715 4839
      </li>
      <li>
        <svg viewBox="0 0 10 10" aria-hidden="true"><path d="M3 0h4a1 1 0 0 1 1 1v8a1 1 0 0 1-1 1H3a1 1 0 0 1-1-1V1a1 1 0 0 1 1-1zM3 1.5v6h4v-6z"/></svg>
        0427 351 604
      </li>
      <li>
        <svg viewBox="0 0 10 10" aria-hidden="true"><path d="M0 2h10v6H0zM1 3v.3l4 2.7 4-2.7V3L5 5.5z"/></svg>
        dale.omar@cushora.com.au
      </li>
      <li>
        <svg viewBox="0 0 10 10" aria-hidden="true"><circle cx="5" cy="5" r="4.5"/></svg>
        www.cushora.com.au
      </li>
    </ul>

    <svg class="corner-bands" viewBox="0 0 480 60" preserveAspectRatio="none" aria-hidden="true">
      <polygon points="330,16 480,16 480,60 360,60" fill="var(--band-grey)"/>
      <polygon points="0,48 330,16 370,16 330,60 0,60" fill="var(--brand-red)"/>
    </svg>
  </section>
</main>
</body>
</html>
```